Minimalist, upmarket hair Pomade Packaging Design

Hi All,

I am planning to start my own pomade brand (hair styling wax). For this one, I would need some help to design bold, upmarket and minimalist design for the packaging. This design is to be printed on the steel box. My initial idea is as per below;

Product: Hair Pomade
Product type:
1. Classic(Medium Hold),
2. Charming (strong hold)
3. Funky(Extra strong hold)
Container: 94*59*21mm metal box
Theme: Bold, upmarket, minimalist
Front design: Have the brand name (kovrit pomade), logo, product type, weight (120g), QR code, include "since 2016",
Back design: usage direction in pictures, ingredients, "made in malaysia" sign, fb, insta, fon number
Updates

Dear Talented Designers, My intent of creating classic, charming n funky is to provide selection to the customer dpending on their lifestyle; classic is for formal but stylish gent, charming for casual and easygoing, and funky for adventure type but love to keep in style type of guy. Maybe you can play around with these concept and highlight these in the front design. I have decided to make the usage of official logo in the front design is OPTIONAL, so unleash your creativity :) official logo is now compulsory to be put at the back design. For the usage instruction, please make it 2D. Thanks

Target Market(s)

Young professional gents

Industry/Entity Type

Hair Care Product

Colors
d2a4cc
f04a50
f37122
fdfeff
000000
ffc214
0493cd
add136
eea4c8

Requirements
Must have
• Qr code integrate with circle logo as attached
Nice to have
• Different colors among product types
Should not have
• Childish look or crowded design

```html
<!DOCTYPE html>
<html lang="en">
<head>
<meta charset="utf-8">
<title>Kovrit Pomade – Hair Pomade Classic Label</title>
<link rel="stylesheet" href="https://fonts.googleapis.com/css2?family=Pacifico&family=Libre+Baskerville:wght@400&family=Poppins:wght@500&display=swap">
<style>
  :root {
    --page: #ffffff;
    --tin-black: #121212;
    --tin-black-soft: #1d1d1d;
    --ink-white: #fdfeff;
    --band-blue: #1f3c96;
    --art-grey: #8a8a8a;
  }
  * { margin: 0; padding: 0; box-sizing: border-box; }
  html, body { width: 1200px; height: 887px; overflow: hidden; background: var(--page); }

  .canvas { position: relative; width: 1200px; height: 887px; }

  .label {
    position: absolute; left: 100px; top: 137px;
    width: 1000px; height: 612px;
    border-radius: 40px;
    background: radial-gradient(ellipse at 50% 45%, var(--tin-black-soft), var(--tin-black) 75%);
    color: var(--ink-white);
  }
  .frame { position: absolute; inset: 0; }

  .brand {
    position: absolute; left: 50%; top: 20px; transform: translateX(-50%);
    display: flex; align-items: center; gap: 18px;
    padding: 8px 18px; background: var(--tin-black);
    white-space: nowrap;
  }
  .brand-mark { width: 56px; height: 56px; background: var(--ink-white); }
  .brand-name {
    font-family: "Libre Baskerville", serif; font-size: 40px; line-height: 48px;
    color: var(--ink-white);
  }
  .brand-tagline {
    border-left: 2px solid var(--ink-white); padding-left: 14px;
    font-family: "Libre Baskerville", serif; font-size: 18px; line-height: 22px;
  }

  .product-name {
    position: absolute; left: 0; right: 0; top: 158px;
    text-align: center; font-family: "Pacifico", cursive; font-weight: 400;
    font-size: 124px; line-height: 170px;
  }
  .variant-band {
    position: absolute; left: 294px; top: 322px; width: 384px; height: 60px;
    background: var(--band-blue);
    display: flex; align-items: center; justify-content: center; gap: 22px;
  }
  .variant-star { width: 20px; height: 20px; fill: var(--ink-white); }
  .variant-name { font-family: "Libre Baskerville", serif; font-size: 46px; letter-spacing: 1px; }
  .hold {
    position: absolute; left: 294px; top: 396px; width: 384px;
    display: flex; align-items: center; gap: 14px;
    font-family: "Libre Baskerville", serif; font-size: 21px; white-space: nowrap;
  }
  .hold::before, .hold::after { content: ""; flex: 1; height: 2px; background: var(--ink-white); }

  .variant-art {
    position: absolute; left: 752px; top: 318px; width: 112px; height: 140px;
    border-radius: 8px;
    background: linear-gradient(160deg, #e9e9e9, var(--art-grey));
  }
  .description {
    position: absolute; left: 118px; top: 480px;
    font-family: "Libre Baskerville", serif; font-size: 22px; white-space: nowrap;
  }
  .net-weight {
    position: absolute; left: 764px; top: 466px;
    font-family: "Poppins", sans-serif; font-weight: 500; font-size: 36px;
  }
</style>
</head>
<body>
<main class="canvas">
  <section class="label">
    <svg class="frame" width="1000" height="612" viewBox="0 0 1000 612" aria-hidden="true">
      <rect x="28" y="28" width="944" height="556" rx="14" fill="none" stroke="#fdfeff" stroke-width="3"/>
      <rect x="42" y="42" width="916" height="528" rx="8" fill="none" stroke="#fdfeff" stroke-width="2"/>
    </svg>

    <div class="brand">
      <span class="brand-mark"></span>
      <span class="brand-name">kovrit pomade</span>
      <span class="brand-tagline">styled for<br>refined gents</span>
    </div>

    <h1 class="product-name">Hair Pomade</h1>

    <div class="variant-band">
      <svg class="variant-star" viewBox="0 0 20 20" aria-hidden="true"><polygon points="10,0 12.9,6.9 20,7.6 14.6,12.4 16.2,19.5 10,15.8 3.8,19.5 5.4,12.4 0,7.6 7.1,6.9"/></svg>
      <span class="variant-name">CLASSIC</span>
      <svg class="variant-star" viewBox="0 0 20 20" aria-hidden="true"><polygon points="10,0 12.9,6.9 20,7.6 14.6,12.4 16.2,19.5 10,15.8 3.8,19.5 5.4,12.4 0,7.6 7.1,6.9"/></svg>
    </div>
    <div class="hold">MEDIUM HOLD</div>

    <div class="variant-art" role="img" aria-label="White line illustration of a gentleman's head with a classic hairstyle"></div>

    <p class="description">Lorem ipsum dolor sit amet loremp ipsum dolor</p>
    <p class="net-weight">120g</p>
  </section>
</main>
</body>
</html>
```